Business Card Design Project - Tall Maple

We are looking for a new business card design. Our company name is Tall Maple Communication Solutions. Our primary function is to provide our clients with communication solutions. These solutions include commercial phone systems and T1 and Fiber Internet lines. Another major part of the business is cabling new buildings with CAT5 cable for both data and phone.

Industry/Entity Type

Communication

Requirements
Must have
• The cards need to be two sided and have some bleeding edge color.
Nice to have
• We are going to upload our current logo BUT we are not married to this logo. If you want to incorporate a re-designed logo with the new business card - please feel free to do so. We are looking for a new bold look that is very colorful yet professional.

```html
<!DOCTYPE html>
<html lang="en">
<head>
<meta charset="utf-8">
<title>Tall Maple Communication Solutions – Business Card</title>
<link rel="stylesheet" href="https://fonts.googleapis.com/css2?family=Arimo:wght@400&family=Noto+Serif:wght@700&display=swap">
<style>
  :root {
    --brand-blue: #1b1f8a;
    --brand-grey: #7b7b7b;
    --text-grey: #6e6e6e;
    --card-white: #ffffff;
    --backdrop: #eceef1;
    --card-w: 540px;
    --card-h: 349px;
  }
  * { box-sizing: border-box; margin: 0; padding: 0; }
  html, body {
    width: 1200px;
    height: 900px;
    overflow: hidden;
    background: var(--backdrop);
  }
  .canvas {
    position: relative;
    width: 1200px;
    height: 900px;
  }
  .card {
    position: absolute;
    top: 275px;
    width: var(--card-w);
    height: var(--card-h);
    background: var(--card-white);
    overflow: hidden;
    box-shadow: 0 6px 18px rgba(20, 24, 60, 0.18);
  }
  .card--front { left: 40px; }
  .card--back { left: 620px; }

  /* Front */
  .front-bg {
    position: absolute;
    inset: 0;
    width: 100%;
    height: 100%;
  }
  .front-brand {
    position: absolute;
    left: 40px;
    top: 128px;
    display: flex;
    align-items: center;
    gap: 22px;
  }
  .brand-dot {
    width: 90px;
    height: 90px;
    border-radius: 50%;
    background: var(--brand-blue);
    flex: none;
  }
  .brand-name {
    font-family: "Arimo", sans-serif;
    font-weight: 400;
    font-size: 30px;
    line-height: 1.15;
    color: var(--brand-blue);
    white-space: nowrap;
  }

  /* Back */
  .back-brand {
    position: absolute;
    left: 26px;
    top: 26px;
    display: flex;
    align-items: center;
    gap: 12px;
  }
  .back-brand .brand-dot { width: 72px; height: 72px; }
  .back-brand .brand-name { font-size: 18px; }

  .contact-lines {
    position: absolute;
    right: 18px;
    top: 42px;
    font-family: "Arimo", sans-serif;
    font-size: 11px;
    color: var(--text-grey);
    border-collapse: collapse;
  }
  .contact-lines td { padding: 1.5px 0; line-height: 1.2; }
  .contact-label { text-align: right; letter-spacing: 0.5px; }
  .contact-dot-cell { width: 22px; text-align: center; }
  .contact-dot {
    display: inline-block;
    width: 5px; height: 5px;
    border-radius: 50%;
    background: var(--brand-grey);
    vertical-align: middle;
  }
  .person {
    position: absolute;
    left: 18px;
    top: 188px;
  }
  .person-name {
    font-family: "Noto Serif", serif;
    font-weight: 700;
    font-size: 15px;
    color: var(--brand-blue);
    margin-bottom: 4px;
  }
  .person-address {
    font-family: "Arimo", sans-serif;
    font-style: normal;
    font-size: 11px;
    line-height: 1.45;
    color: var(--text-grey);
  }
  .back-band {
    position: absolute;
    left: 0; right: 0; bottom: 0;
    height: 46px;
    background: var(--brand-blue);
  }
</style>
</head>
<body>
<main class="canvas">

  <section class="card card--front" aria-label="Business card front">
    <svg class="front-bg" viewBox="0 0 540 349" preserveAspectRatio="none" aria-hidden="true">
      <rect width="540" height="349" fill="var(--brand-blue)"/>
      <ellipse cx="266" cy="176" rx="292" ry="196" fill="var(--card-white)"/>
    </svg>
    <div class="front-brand">
      <span class="brand-dot" aria-hidden="true"></span>
      <p class="brand-name">Tall Maple<br>Communication Solutions</p>
    </div>
  </section>

  <section class="card card--back" aria-label="Business card back">
    <div class="back-brand">
      <span class="brand-dot" aria-hidden="true"></span>
      <p class="brand-name">Tall Maple</p>
    </div>

    <table class="contact-lines">
      <tr><td class="contact-label">OFFICE</td><td class="contact-dot-cell"><span class="contact-dot"></span></td><td>555.014.2203</td></tr>
      <tr><td class="contact-label">CELL</td><td class="contact-dot-cell"><span class="contact-dot"></span></td><td>555.016.4478</td></tr>
      <tr><td class="contact-label">24/7</td><td class="contact-dot-cell"><span class="contact-dot"></span></td><td>555.019.3361</td></tr>
      <tr><td class="contact-label">FAX</td><td class="contact-dot-cell"><span class="contact-dot"></span></td><td>555.012.8805</td></tr>
    </table>

    <div class="person">
      <p class="person-name">Dana Whitfield</p>
      <address class="person-address">
        1480 W Juniper Avenue<br>
        Suite 210<br>
        Cedar Falls, AZ 85099
      </address>
    </div>

    <div class="back-band"></div>
  </section>

</main>
</body>
</html>
```